Professional Mothers Wordpress Site

*** To be clear, as a result of this contest I am looking for a fully functioning wordpress site to import into my wordpress site. Not just an image layout design.***

A Responsive Wordpress Blog Site for Professional Mothers

List of features desired:
1. Social media platform and commenting
2. Fully featured ecommerce store
3. Create and display fantastic-looking galleries of vimeo video content
4. Customised slideshows that are displayed in a content slider. Slides can be filled with text, images, video, social media stream feeds and syndicated content like Trillpost feeds, YouTube, Pinterest, Flickr and more.
5. HTML5 and Flash compatible audio player that sits within the site. Works across both desktop and mobile devices
6. Admin panel
7. Google docs integrated email subscription, forms etc., email opt-in for newsletter
8. URL shortener
9. Enhanced image gallery
10. Interactive drag-and-drop pricing tables
11. Google Analytics, sitemaps
12. Rating system

List of pages on blogsite
1. Home page
2. About page
3. Resources page
4. Podcast archive page
5. Coaching page
6. Contact page

Here are some things I liked about the blogs I clicked through (and why I did or didn't like them)

Examples:
1) http://www.brindlepath.com/‎ - clean, professional feel
2) http://www.tessagrunwick.com/ - i like the simplicity of the email sign up and how it stands out without being obnoxious
3) http://velantrocast.com/ - i like the simplicity of the links to various pages at the top
4) http://www.quillsetworks.com/ - i like how the links are clear at the top and how they stay still even if the page moves (persistent headers)
5) http://www.makerstidehourly.com/ - i like how the podcast sessions are laid out on the front page
6) http://www.calvendo.com/ - this has a really nice 1st impression
7) http://uncleskiptrack.com/ - this has a nice layout too but the logo is way too big and it takes too long to scroll down to the content
8) http://zenbix.com/ - I like the moving content of this

Overall I'm going for something neat, clean and simple.

Target Market(s)

Working Mothers

Industry/Entity Type

Store

Requirements
Must have
• The social media links at the top of the page

```html
<!DOCTYPE html>
<html lang="en">
<head>
<meta charset="utf-8">
<title>Hearthwork Mums</title>
<link rel="stylesheet" href="https://fonts.googleapis.com/css2?family=Source+Sans+3:wght@300;400;600&display=swap">
<style>
:root{
  --ink:#231f20;
  --plum:#8e1f74;
  --magenta:#a8328f;
  --pink-light:#d98ac4;
  --pink-mid:#c05aa8;
  --text:#333;
  --muted:#6b6b6b;
  --rule:#bbb;
  --white:#fff;
  --footer:#f1f1f1;
  --star-off:#cfcfcf;
}
*{box-sizing:border-box;margin:0;padding:0}
html,body{width:1200px;height:2256px;overflow:hidden}
body{position:relative;background:var(--white);font-family:"Source Sans 3",Arial,sans-serif;color:var(--text)}
.abs{position:absolute}

.site-header{left:0;top:0;width:1200px;height:131px;background:var(--ink)}
.brand{left:88px;top:22px;display:flex;align-items:center;gap:12px;color:#c33ba3;font-size:40px;font-weight:400;line-height:1}
.brand-dot{width:40px;height:40px;border-radius:50%;background:#c33ba3}
.social-top{right:110px;top:11px;display:flex;gap:6px}
.social-top span{width:29px;height:29px;border-radius:50%;display:block}
.main-nav{right:90px;top:70px;display:flex;font-size:21px;color:var(--white)}
.main-nav a{color:inherit;text-decoration:none;padding:0 22px;border-left:1px solid #555;line-height:24px}
.main-nav a:first-child{border-left:0}

.hero{left:0;top:131px;width:1200px;height:422px;background:linear-gradient(90deg,#eef0ee 0%,#e2e4e0 45%,#cfd3ce 65%,#9fb89a 100%)}
.hero-card{left:80px;top:160px;width:355px;height:370px;background:var(--white);border-radius:8px;box-shadow:0 2px 8px rgba(0,0,0,.15);padding:30px 26px}
.hero-card h2{font-size:18px;font-weight:600;color:var(--plum)}
.hero-card p{font-size:15px;color:var(--muted);line-height:20px;margin-top:2px}
.video{margin-top:20px;width:313px;height:181px;background:linear-gradient(135deg,#d8b78e,#e7c75a 60%,#9fc36e);position:relative}
.play{position:absolute;left:133px;top:66px;width:46px;height:46px;border-radius:50%;background:#222;border:3px solid #fff}
.play::after{content:"";position:absolute;left:17px;top:11px;border-left:15px solid #fff;border-top:9px solid transparent;border-bottom:9px solid transparent}
.share-row{display:flex;gap:8px;margin-top:20px}
.share{font-size:11px;color:#3b5998;border:1px solid #c9c9c9;border-radius:2px;padding:1px 5px;background:#f4f6fa;line-height:14px;display:inline-block}
.count{font-size:10px;color:#555;border:1px solid #ccc;padding:1px 4px;line-height:14px}
.hero-arrows{left:1064px;top:495px}

.signup{left:0;top:553px;width:1200px;height:85px;background:linear-gradient(180deg,#d07dbd,#a8328f);display:flex;align-items:center}
.signup h3{position:absolute;left:142px;top:26px;font-size:27px;font-weight:300;color:var(--white)}
.field{position:absolute;top:29px;height:32px;background:var(--white);border-radius:3px;font-size:14px;color:#777;padding:7px 12px}
.btn-signup{position:absolute;left:970px;top:28px;width:89px;height:34px;background:#7e1463;color:var(--white);border-radius:3px;font-size:16px;text-align:center;line-height:33px}

.section-title{left:82px;top:678px;font-size:25px;font-weight:600;color:var(--plum)}
.podcast{left:82px;width:673px;display:flex;gap:19px}
.podcast-thumb{width:250px;height:228px;flex:none}
.podcast-body{width:404px;margin-top:-2px}
.podcast-body h4{font-size:25px;font-weight:400;color:var(--ink);line-height:28px;margin-bottom:8px}
.podcast-body p{font-size:14.5px;line-height:22.5px;color:var(--text);margin-bottom:6px}
.meta{font-size:14.5px;color:var(--plum);margin:10px 0 12px}
.mini-shares{display:flex;gap:8px}
.divider{left:82px;width:673px;border-top:2px dotted var(--rule)}

.panel{left:787px;width:330px;border-radius:5px;background:linear-gradient(180deg,var(--pink-light),var(--magenta))}
.panel h3{position:absolute;left:27px;top:18px;font-size:24px;font-weight:400;color:var(--white)}
.panel-inner{position:absolute;left:21px;width:289px;background:var(--white);border-radius:4px}
.panel-more{position:absolute;right:22px;font-size:13px;color:#f3d7eb}
.review{padding:18px 20px 12px;border-bottom:1px solid #ddd;margin:0 0}
.review:last-child{border-bottom:0}
.review h5{font-size:15px;font-weight:600;color:var(--ink);margin-bottom:2px}
.review p{font-size:14px;line-height:22px;color:var(--muted)}
.rating{display:flex;align-items:center;gap:6px;font-size:14.5px;color:var(--plum);margin-top:6px}
.rating svg{margin-right:14px}
.post{display:flex;gap:12px;padding:20px 0 0 19px}
.avatar{width:74px;height:66px;border-radius:3px;flex:none}
.post h5{font-size:14px;font-weight:600;color:var(--ink);line-height:18px}
.post p{font-size:12px;line-height:16px;color:var(--muted);width:160px}
.post .when{color:var(--plum);font-size:12px}

.site-footer{left:0;top:2160px;width:1200px;height:96px;background:linear-gradient(180deg,#fafafa,var(--footer))}
.site-footer p{position:absolute;left:90px;top:38px;font-size:14px;color:#555}
</style>
</head>
<body>

<header class="site-header abs">
  <div class="brand abs"><span class="brand-dot"></span>Hearthwork Mums</div>
  <div class="social-top abs" aria-label="Social links">
    <span style="background:#29a9e0"></span><span style="background:#cb2027"></span><span style="background:#3b5998"></span><span style="background:#3fc1e8"></span><span style="background:#1a8dc4"></span>
  </div>
  <nav class="main-nav abs"><a href="#">Home</a><a href="#">About me</a><a href="#">Podcasts</a><a href="#">Resources</a><a href="#">Contact</a></nav>
</header>

<section class="hero abs" role="img" aria-label="Photo of a mother working at a laptop while holding her sleeping baby"></section>
<div class="hero-card abs">
  <h2>Duis tincidunt lectus quis viverra</h2>
  <p>Mauris vel lacus vitae felis vestibulum volutpat. Etiam est nunc, venenatis tristique</p>
  <div class="video" role="img" aria-label="Video still of a mother and daughter smiling outdoors"><span class="play"></span></div>
  <div class="share-row"><span class="share">Like</span><span class="count">3k</span><span class="share">Post</span><span class="count">316</span><span class="share">Share</span><span class="count">6</span><span class="share" style="color:#cb2027">Save</span><span class="count">5</span></div>
</div>
<svg class="hero-arrows abs" width="50" height="36" viewBox="0 0 50 36" aria-hidden="true"><path d="M16 2 4 18l12 16M34 2l12 16-12 16" fill="none" stroke="#fff" stroke-width="2.5"/></svg>

<section class="signup abs">
  <h3>Sign up and receive our free e-book</h3>
  <div class="field" style="left:531px;width:207px">First name</div>
  <div class="field" style="left:752px;width:206px">email address</div>
  <div class="btn-signup">Sign Up</div>
</section>

<h2 class="section-title abs">Podcasts</h2>

<article class="podcast abs" style="top:727px">
  <div class="podcast-thumb" role="img" aria-label="Photo of a mother with a baby and child at a laptop in the kitchen" style="background:linear-gradient(135deg,#d9dde0,#b9c7d6 55%,#e9d8c6)"></div>
  <div class="podcast-body">
    <h4>Duis tincidunt lectus quis viverra vestibulum</h4>
    <p>Nunc tempus felis vitae urna. Vivamus porttitor, g, purus nisi eleifend libero, a tempus libero lectus feugiat felis.</p>
    <p>Morbi diam mauris, viverra in, gravida eu, mattis in, ante. Morbi eget arcu. Morbi porta, libero id ullamcorper nonummy, nibh ligula pulvinar metus, eget consectetuer augue nisi quis lacus. Curabitur vel mi sit amet magna malesuada ultrices. Ut nisi erat, fermentum vel, congue id, euismod in, elit. Fusce ultricies, orci ac feugiat suscipit, leo massa sodales velit</p>
    <div class="meta">Learn More &nbsp;|&nbsp; Posted on 1st June 2013</div>
    <div class="mini-shares"><span class="share">Like</span><span class="share">Post</span><span class="share" style="color:#dd4b39">+1</span><span class="share" style="color:#cb2027">Save</span></div>
  </div>
</article>
<div class="divider abs" style="top:1067px"></div>

<article class="podcast abs" style="top:1100px">
  <div class="podcast-thumb" role="img" aria-label="Photo of a mother reading a book with her toddler" style="background:linear-gradient(135deg,#e8e2d6,#e4c98f 50%,#f2ede6)"></div>
  <div class="podcast-body">
    <h4>Aliquam vehicula mi at mauris</h4>
    <p>Nunc tempus felis vitae urna. Vivamus porttitor, g, purus nisi eleifend libero, a tempus libero lectus feugiat felis.</p>
    <p>Morbi diam mauris, viverra in, gravida eu, mattis in, ante. Morbi eget arcu. Morbi porta, libero id ullamcorper nonummy, nibh ligula pulvinar metus, eget consectetuer augue nisi quis lacus. Curabitur vel mi sit amet magna malesuada ultrices. Ut nisi erat, fermentum vel, congue id, euismod in, elit. Fusce ultricies, orci ac feugiat suscipit, leo massa sodales velit</p>
    <div class="meta">Learn More &nbsp;|&nbsp; Posted on 1st June 2013</div>
    <div class="mini-shares"><span class="share">Like</span><span class="share">Post</span><span class="share" style="color:#dd4b39">+1</span><span class="share" style="color:#cb2027">Save</span></div>
  </div>
</article>
<div class="divider abs" style="top:1407px"></div>

<article class="podcast abs" style="top:1440px">
  <div class="podcast-thumb" role="img" aria-label="Photo of a mother holding a baby while using a laptop" style="background:linear-gradient(135deg,#d7cfc4,#ecd9d2 50%,#c73a5c 80%,#eee)"></div>
  <div class="podcast-body">
    <h4>Curabitur vel mi sit amet magna</h4>
    <p>Nunc tempus felis vitae urna. Vivamus porttitor, g, purus nisi eleifend libero, a tempus libero lectus feugiat felis.</p>
    <p>Morbi diam mauris, viverra in, gravida eu, mattis in, ante. Morbi eget arcu. Morbi porta, libero id ullamcorper nonummy, nibh ligula pulvinar metus, eget consectetuer augue nisi quis lacus. Curabitur vel mi sit amet magna malesuada ultrices. Ut nisi erat, fermentum vel, congue id, euismod in, elit. Fusce ultricies, orci ac feugiat suscipit, leo massa sodales velit</p>
    <div class="meta">Learn More &nbsp;|&nbsp; Posted on 1st June 2013</div>
    <div class="mini-shares"><span class="share">Like</span><span class="share">Post</span><span class="share" style="color:#dd4b39">+1</span><span class="share" style="color:#cb2027">Save</span></div>
  </div>
</article>
<div class="divider abs" style="top:1747px"></div>

<article class="podcast abs" style="top:1778px">
  <div class="podcast-thumb" role="img" aria-label="Photo of a mother in office wear reading papers beside her child" style="background:linear-gradient(135deg,#e6e6e6,#bfc3c8 50%,#5a8fb3 85%)"></div>
  <div class="podcast-body">
    <h4>Duis tincidunt lectus quis viverra vestibulum</h4>
    <p>Nunc tempus felis vitae urna. Vivamus porttitor, g, purus nisi eleifend libero, a tempus libero lectus feugiat felis.</p>
    <p>Morbi diam mauris, viverra in, gravida eu, mattis in, ante. Morbi eget arcu. Morbi porta, libero id ullamcorper nonummy, nibh ligula pulvinar metus, eget consectetuer augue nisi quis lacus. Curabitur vel mi sit amet magna malesuada ultrices. Ut nisi erat, fermentum vel, congue id, euismod in, elit. Fusce ultricies, orci ac feugiat suscipit, leo massa sodales velit</p>
    <div class="meta">Learn More &nbsp;|&nbsp; Posted on 1st June 2013</div>
    <div class="mini-shares"><span class="share">Like</span><span class="share">Post</span><span class="share" style="color:#dd4b39">+1</span><span class="share" style="color:#cb2027">Save</span></div>
  </div>
</article>

<svg width="0" height="0" style="position:absolute">
  <defs>
    <symbol id="star" viewBox="0 0 20 20"><path d="M10 1l2.7 5.6 6.1.9-4.4 4.3 1 6.1L10 15l-5.4 2.9 1-6.1L1.2 7.5l6.1-.9z"/></symbol>
  </defs>
</svg>

<aside class="panel abs" style="top:676px;height:766px">
  <h3>Link to Tunevault</h3>
  <div class="panel-inner" style="top:61px;height:661px">
    <div class="review">
      <h5>Tittle line goes here</h5>
      <p>Nunc tempus felis vitae urna. Vivamus porttitor, g, purus nisi eleifend libero, a tempus libero lectus feugiat felis.</p>
      <div class="rating">Rating <svg width="84" height="14"><g fill="var(--plum)"><use href="#star" width="14" height="14"/><use href="#star" x="17" width="14" height="14"/><use href="#star" x="34" width="14" height="14"/></g><g fill="var(--star-off)"><use href="#star" x="51" width="14" height="14"/><use href="#star" x="68" width="14" height="14"/></g></svg>Review 24</div>
    </div>
    <div class="review">
      <h5>Tittle line goes here</h5>
      <p>Nunc tempus felis vitae urna. Vivamus porttitor, g, purus nisi eleifend libero, a tempus libero lectus feugiat felis.</p>
      <div class="rating">Rating <svg width="84" height="14"><g fill="var(--plum)"><use href="#star" width="14" height="14"/><use href="#star" x="17" width="14" height="14"/><use href="#star" x="34" width="14" height="14"/></g><g fill="var(--star-off)"><use href="#star" x="51" width="14" height="14"/><use href="#star" x="68" width="14" height="14"/></g></svg>Review 19</div>
    </div>
    <div class="review">
      <h5>Tittle line goes here</h5>
      <p>Nunc tempus felis vitae urna. Vivamus porttitor, g, purus nisi eleifend libero, a tempus libero lectus feugiat felis.</p>
      <div class="rating">Rating <svg width="84" height="14"><g fill="var(--plum)"><use href="#star" width="14" height="14"/><use href="#star" x="17" width="14" height="14"/></g><g fill="var(--star-off)"><use href="#star" x="34" width="14" height="14"/><use href="#star" x="51" width="14" height="14"/><use href="#star" x="68" width="14" height="14"/></g></svg>Review 20</div>
    </div>
    <div class="review">
      <h5>Tittle line goes here</h5>
      <p>Duis tincidunt lectus quis dui viverra vestibulum. Suspendisse vulputate aliquam dui. Nulla elementum dui ut augue. Aliquam vehicula mi at mauris. Maecenas placerat, nisl at consequat rhoncus, sem nunc gravida justo, quis</p>
      <div class="rating">Rating <svg width="84" height="14"><g fill="var(--plum)"><use href="#star" width="14" height="14"/><use href="#star" x="17" width="14" height="14"/><use href="#star" x="34" width="14" height="14"/></g><g fill="var(--star-off)"><use href="#star" x="51" width="14" height="14"/><use href="#star" x="68" width="14" height="14"/></g></svg>Review 19</div>
    </div>
  </div>
  <span class="panel-more" style="top:734px">Click here for more reviews</span>
</aside>

<aside class="panel abs" style="top:1455px;height:470px">
  <h3 style="top:14px;font-size:22px">Trillpost Feed</h3>
  <div class="panel-inner" style="top:51px;height:374px">
    <div class="post"><div class="avatar" role="img" aria-label="Author portrait" style="background:linear-gradient(135deg,#8a7d70,#cfc6bb)"></div><div><h5>Blog Tittle here</h5><p>Duis tincidunt lectus quis dui viverra Suspendisse vulputate</p><p class="when">&#9656; Posted on May, 28 2013</p></div></div>
    <div class="post"><div class="avatar" role="img" aria-label="Author portrait" style="background:linear-gradient(135deg,#3f6a8a,#d7a878)"></div><div><h5>Blog Tittle here</h5><p>Duis tincidunt lectus quis dui viverra Suspendisse vulputate</p><p class="when">&#9656; Posted on May, 25 2013</p></div></div>
    <div class="post"><div class="avatar" role="img" aria-label="Author portrait" style="background:linear-gradient(135deg,#e8e1d8,#b9784f)"></div><div><h5>Blog Tittle here</h5><p>Duis tincidunt lectus quis dui</p><p class="when">&#9656; Posted on May, 21 2013</p></div></div>
    <div class="post"><div class="avatar" role="img" aria-label="Author portrait" style="background:linear-gradient(135deg,#d9d6d2,#c59d86)"></div><div><h5>Blog Tittle here</h5><p>Duis tincidunt lectus quis dui</p><p class="when">&#9656; Posted on May, 15 2013</p></div></div>
  </div>
  <span class="panel-more" style="top:441px">View more Blog Post</span>
</aside>

<footer class="site-footer abs"><p>&copy; 2013 Company Name. &nbsp;All right reserved. &nbsp;Term of Use.</p></footer>

</body>
</html>
```